Sonne im Glas
Zielgruppe
Wir sind ein kleines Weingut in einer kleinen Ortschaft am Neusiedlersee | Burgenland | Österreich und produzieren auf unseren Weingartenflächen zertifizierte Bioweine.
Die Zielgruppe für diesen außergewöhnlichen Wein sind Weininteressierte im mittleren Alter.
Aufgabenstellung
Name des Weines: 'Sonne im Glas'
Es handelt sich um einen Wein einer lokalen Sorte der nach der händischen Ernte und Spontanvergärung von September bis Juni des folgenden Jahres (also 10 Monate) auf der Feinhefe und ohne Eingriffe gelagert hat. Dannach erfolgt die Füllung ohne Filtration.
Dementsprechend chillig, vielschichtig und harmonisch präsentiert sich dieser Wein jetzt nach der Füllung in Burgunderflaschen.
Etikettendimension soll in der Richtung: 100 x 80 (HxB) liegen, wobei die Höhe mit 100 mm begrenzend ist.

```html
<!DOCTYPE html>
<html lang="de">
<head>
<meta charset="utf-8">
<title>Sonne im Glas – Etikett</title>
<link rel="stylesheet" href="https://fonts.googleapis.com/css2?family=Didact+Gothic&family=Kaushan+Script&display=swap">
<style>
  :root {
    --wine: #7a0d07;
    --wine-title: #7d1a12;
    --paper: #ffffff;
    --band-text: #f3dcd6;
    --vine-light: #f6e7e4;
    --vine-mid: #e9cdc8;
  }
  * { margin: 0; padding: 0; box-sizing: border-box; }
  html, body {
    width: 1200px;
    height: 959px;
    overflow: hidden;
    background: var(--paper);
  }
  .label {
    position: relative;
    width: 1200px;
    height: 959px;
    background: var(--paper);
    overflow: hidden;
  }
  .vine-illustration {
    position: absolute;
    left: 520px;
    top: 30px;
    width: 640px;
    height: 750px;
    border-radius: 320px 320px 0 0;
    background: radial-gradient(ellipse at 55% 40%, var(--vine-mid) 0%, var(--vine-light) 55%, rgba(255,255,255,0) 80%);
  }
  .wine-name {
    position: absolute;
    left: 42px;
    top: 390px;
    color: var(--wine-title);
    font-family: "Didact Gothic", "Century Gothic", sans-serif;
    font-weight: 400;
    line-height: 1;
  }
  .wine-name__line {
    display: block;
    white-space: nowrap;
  }
  .wine-name__word {
    font-size: 142px;
    letter-spacing: 1px;
  }
  .wine-name__accent {
    font-family: "Kaushan Script", cursive;
    font-size: 130px;
    margin-left: 18px;
  }
  .wine-name__line--second {
    margin-left: 296px;
    margin-top: 12px;
  }
  .tagline-band {
    position: absolute;
    left: 0;
    top: 780px;
    width: 1200px;
    height: 179px;
    background: var(--wine);
    display: flex;
    align-items: center;
    justify-content: center;
  }
  .tagline {
    color: var(--band-text);
    font-family: "Didact Gothic", "Century Gothic", sans-serif;
    font-size: 31px;
    letter-spacing: 0.5px;
    margin-left: -20px;
  }
</style>
</head>
<body>
  <main class="label">
    <div class="vine-illustration" role="img" aria-label="Rebranke mit Blättern und zwei Weintrauben in Weinrot"></div>

    <h1 class="wine-name">
      <span class="wine-name__line"><span class="wine-name__word">Sonne</span><span class="wine-name__accent">im</span></span>
      <span class="wine-name__line wine-name__line--second"><span class="wine-name__word">Glas</span></span>
    </h1>

    <footer class="tagline-band">
      <p class="tagline">Lokaler Biowein aus händischer Ernte</p>
    </footer>
  </main>
</body>
</html>
```